Runlark

I have a web site RUNLARK.com that is in serious need of a re-design. The site is mean't to be a portal for an app that I have called RUNLARK which you can see in the app store or googleplay. Take a look and see what you can do.
Updates

Project Deadline Extended
Reason: Still working with designers. The "look" is not quite there but a lot of progress has been made. MB

Industry/Entity Type

Store

```html
<!DOCTYPE html>
<html lang="en">
<head>
<meta charset="utf-8">
<title>Runlark – Sport stats on demand</title>
<link rel="stylesheet" href="https://fonts.googleapis.com/css2?family=Open+Sans:wght@400;600;700;800&family=Shadows+Into+Light&display=swap">
<style>
:root{
  --green:#1f9a3a;
  --green-dark:#146b28;
  --nav:#1d5f2e;
  --navy:#0f1a33;
  --ink:#111;
  --panel:#2b2b2b;
  --light:#e3e3e3;
  --grey:#8b8b8b;
  --white:#fff;
  --blue:#1d5fb0;
}
*{box-sizing:border-box;margin:0;padding:0}
html,body{width:699px;height:1200px;overflow:hidden}
body{font-family:"Open Sans",Arial,sans-serif;background:var(--white);color:var(--ink);position:relative}
.site-header{height:64px;position:relative;background:var(--white)}
.brand{position:absolute;left:120px;top:14px;display:flex;align-items:center;gap:10px}
.brand-dot{width:26px;height:26px;border-radius:50%;background:var(--green)}
.brand-name{font-size:30px;font-weight:800;color:var(--blue);letter-spacing:.5px}
.social{position:absolute;right:38px;top:10px;display:flex;gap:4px}
.social span{width:14px;height:14px;background:var(--blue)}
.social span:nth-child(2){background:#3aa0e0}
.social span:nth-child(3){background:#d23c2c}
.social span:nth-child(4){background:#888}
.top-search{position:absolute;right:38px;top:30px;width:62px;height:12px;border:1px solid #bbb}
.main-nav{height:26px;background:var(--nav);display:flex;justify-content:space-around;align-items:center;padding:0 20px}
.main-nav a{color:var(--white);font-size:11px;font-weight:600;text-decoration:none}
.hero{height:242px;background:var(--navy);position:relative;color:var(--white)}
.hero h1{position:absolute;left:64px;top:34px;width:380px;font-size:19px;font-weight:700;line-height:1.35;text-align:center}
.photo-strip{position:absolute;left:66px;top:142px;display:flex;gap:6px}
.photo-strip div{width:94px;height:56px;background:linear-gradient(135deg,#3f6d3c,#a9b7a0)}
.hero-phones{position:absolute;left:452px;top:24px;width:170px;height:178px;background:linear-gradient(160deg,#3c3c3c,#d9dde2 55%,#2a2a2a);border-radius:10px}
.store-badge{position:absolute;width:128px;height:34px;background:#000;border:1px solid #777;border-radius:5px}
.hero .store-badge{left:468px;top:214px}
.grass{height:204px;position:relative;background:linear-gradient(180deg,#2c5a22,#4e8f33 60%,#2f6b24);color:var(--white)}
.grass-overlay{position:absolute;left:52px;top:0;width:300px;height:204px;background:rgba(10,20,10,.55);padding:14px 14px}
.grass h2{font-size:22px;font-weight:800;line-height:1.1}
.grass p{font-size:8.5px;line-height:1.35;margin:6px 0 10px}
.grass .avail{font-size:9px;font-weight:700;line-height:1.3}
.grass .store-badge{left:200px;top:152px}
.options-band{height:268px;display:flex}
.on-demand{width:196px;background:var(--panel);color:var(--white);padding:30px 20px}
.on-demand h2{font-size:17px;font-weight:700;line-height:1.25;margin-bottom:14px}
.on-demand p{font-size:11px;line-height:1.45;color:#ddd}
.options{flex:1;background:var(--light);position:relative}
.options h2{position:absolute;left:160px;top:8px;font-size:26px;font-weight:700;letter-spacing:.5px}
.options-phone{position:absolute;left:200px;top:56px;width:96px;height:176px;background:linear-gradient(180deg,#222,#eef1f4 30%,#cfd6e0 80%,#222);border-radius:10px}
.options .note{position:absolute;font-family:"Shadows Into Light",cursive;font-size:15px;color:#444}
.options svg{position:absolute;left:0;top:0}
.features{height:364px;background:var(--grey);display:flex;justify-content:center;gap:20px;padding-top:54px}
.feature-card{width:174px;height:306px;background:var(--green);padding:12px 10px;display:flex;flex-direction:column;align-items:center}
.feature-text{background:var(--ink);color:var(--white);width:100%;height:240px;padding:14px 10px;font-size:9px;line-height:1.4;text-align:center}
.feature-text h3{font-size:10px;font-weight:700;margin-bottom:10px;line-height:1.3}
.feature-card .free{margin-top:18px;font-weight:700;font-size:11px;color:var(--white)}
.site-footer{height:32px;background:#000;color:var(--white);display:flex;align-items:center;justify-content:space-between;padding:0 64px 0 40px;font-size:9px}
.site-footer ul{list-style:none;line-height:1.2}
.foot-search{width:130px;height:14px;background:var(--white);color:#777;font-size:8px;padding:1px 4px}
</style>
</head>
<body>
<header class="site-header">
  <div class="brand"><span class="brand-dot"></span><span class="brand-name">Runlark</span></div>
  <div class="social"><span></span><span></span><span></span><span></span></div>
  <div class="top-search"></div>
</header>
<nav class="main-nav">
  <a href="#">Team Statistics</a><a href="#">Player Background</a><a href="#">Live Scores</a><a href="#">Schedules</a><a href="#">Player Performance</a>
</nav>
<section class="hero">
  <h1>The sport statistics and information you want when you want them<br>Watching a sporting event and need information?</h1>
  <div class="photo-strip">
    <div role="img" aria-label="Football players on the field"></div>
    <div role="img" aria-label="Basketball game action"></div>
    <div role="img" aria-label="Soccer match in play"></div>
    <div role="img" aria-label="Hockey players on ice"></div>
  </div>
  <div class="hero-phones" role="img" aria-label="Two phones showing the app's stats screens"></div>
  <div class="store-badge" role="img" aria-label="App Market download badge"></div>
</section>
<section class="grass" role="img" aria-label="Person relaxing on a grass field watching a game">
  <div class="grass-overlay">
    <h2>END THE HASSLE!</h2>
    <p>Stop jumping between different websites to find live scores, player stats, schedules and past game performances. It's all here in one app, ready when you are. Open it at any stadium or sofa and pick your sport, league and team in seconds.</p>
    <h2>GET THE NUMBERS!</h2>
    <p>Stats for pro and college leagues, plus international soccer. More sports coming soon.</p>
    <div class="avail">AVAILABLE ON<br>APP MARKET</div>
  </div>
  <div class="store-badge"></div>
</section>
<section class="options-band">
  <div class="on-demand">
    <h2>Sport Stats on Demand</h2>
    <p>Forget about relying on sport casters or the banner moving on the bottom of your screen for the scores you want. Just select your league, go to team data, go to the game you're interested in and get the score. All in a matter of seconds.</p>
  </div>
  <div class="options">
    <h2>FULL OF OPTIONS</h2>
    <div class="options-phone" role="img" aria-label="Phone showing the app's league menu"></div>
    <svg width="503" height="268" viewBox="0 0 503 268" fill="none" stroke="#555" stroke-width="1.2">
      <path d="M150 90 L196 96"/><path d="M150 130 L196 132"/><path d="M150 170 L196 168"/><path d="M150 222 L196 206"/>
      <path d="M300 80 L350 72"/><path d="M300 118 L350 110"/><path d="M300 160 L350 162"/><path d="M300 200 L350 216"/>
    </svg>
    <span class="note" style="left:40px;top:74px">get venue<br>information</span>
    <span class="note" style="left:46px;top:120px">get the schedule</span>
    <span class="note" style="left:52px;top:160px">get team stats</span>
    <span class="note" style="left:40px;top:214px">get player stats</span>
    <span class="note" style="left:356px;top:62px">select your league</span>
    <span class="note" style="left:356px;top:102px">select your team</span>
    <span class="note" style="left:356px;top:150px">find out who<br>reffed the game</span>
    <span class="note" style="left:356px;top:210px">get live scores</span>
  </div>
</section>
<section class="features">
  <article class="feature-card">
    <div class="feature-text"><h3>On the Go and you need to know</h3>Not a problem. At the game or on the road, the scores you want are only a tap away. Just open the app and you are set.</div>
    <span class="free">FREE</span>
  </article>
  <article class="feature-card">
    <div class="feature-text"><h3>How You Can Beat Watching a Game and Need to Know More about a Team or Player</h3>If you are watching a game and want to know how another competition is shaping up or you want to find out how a team or player's doing this season, just check the app. You get the stats you want without leaving the game.</div>
    <span class="free">FREE</span>
  </article>
  <article class="feature-card">
    <div class="feature-text"><h3>Perfect for the fantasy game player. Get team and player stats from previous games fast</h3>No need to go through reports or stats from other apps; the information is all in one spot to make your fantasy picks easier, faster and smarter.</div>
    <span class="free">FREE</span>
  </article>
</section>
<footer class="site-footer">
  <ul><li>Help</li><li>CONTACT US</li></ul>
  <div class="foot-search">Search</div>
</footer>
</body>
</html>
```